Real Estate investment company needs billboard designs

This is our website: https://velmarkpropertygroup.com/
We are looking for some billboard concepts that uses our CEO in the design. I have attached some images and 1 billboard design that someone in our industry uses, but we don't want it exactly like his.

Industry/Entity Type

real estate

Colors

Designer to choose colors to be used in the design.

Requirements
Must have
• Company colors from websiute

```html
<!DOCTYPE html>
<html lang="en">
<head>
<meta charset="UTF-8">
<title>Velmark Property Group – Billboard</title>
<link rel="stylesheet" href="https://fonts.googleapis.com/css2?family=Oswald:wght@700&family=Montserrat:wght@600;700;800&display=swap">
<style>
  :root {
    --navy: #1c2466;
    --navy-deep: #121a4a;
    --red: #f1141b;
    --ink: #1c1c1c;
    --white: #ffffff;
    --page: #e9ecf1;
    --photo-light: #f1f1f1;
    --photo-mid: #cfcfcf;
    --person-tone: #a9b2cf;
  }
  * { margin: 0; padding: 0; box-sizing: border-box; }
  html, body { width: 1200px; height: 1200px; overflow: hidden; }
  body { background: var(--page); position: relative; }

  .billboard {
    position: absolute;
    left: 40px; top: 345px;
    width: 1120px; height: 510px;
    overflow: hidden;
    background: linear-gradient(180deg, var(--photo-light) 0%, var(--photo-mid) 100%);
    box-shadow: 0 6px 24px rgba(0,0,0,.18);
  }
  .house-photo {
    position: absolute; left: 300px; top: 90px; width: 800px; height: 420px;
    background: linear-gradient(180deg, #e4e4e4 0%, #c8c8c8 100%);
    opacity: .7;
  }
  .brand {
    position: absolute; left: 42px; top: 34px;
    font-family: "Montserrat", sans-serif; font-weight: 700; color: var(--navy);
    line-height: 1;
  }
  .brand-name { font-size: 46px; letter-spacing: 2px; display: block; }
  .brand-sub { font-size: 16px; letter-spacing: 4.4px; display: block; margin-top: 6px; }

  .ceo-photo {
    position: absolute; left: 30px; top: 170px; width: 260px; height: 340px;
    background: linear-gradient(180deg, #c9cfe1 0%, var(--person-tone) 100%);
    border-radius: 110px 110px 0 0;
    z-index: 3;
  }

  .headline {
    position: absolute; left: 345px; top: 66px;
    font-family: "Oswald", sans-serif; font-weight: 700; line-height: 1.02;
    letter-spacing: -1px;
  }
  .headline-main { font-size: 94px; color: var(--navy); display: block; }
  .headline-sub { font-size: 64px; color: var(--navy-deep); display: block; }
  .headline-sub .accent { color: var(--red); }

  .offer-box {
    position: absolute; left: 482px; top: 282px;
    border: 4px solid var(--red); border-radius: 12px;
    padding: 4px 20px;
    font-family: "Montserrat", sans-serif; font-weight: 800; font-size: 34px;
    line-height: 1.2;
    color: var(--navy-deep); letter-spacing: 1px;
  }
  .offer-box .accent { color: var(--red); }

  .phone {
    position: absolute; left: 405px; top: 350px;
    display: flex; align-items: center; gap: 14px;
    font-family: "Montserrat", sans-serif; font-weight: 800; font-size: 80px;
    line-height: 1;
    color: var(--ink); letter-spacing: -1px;
    z-index: 2;
  }
  .phone-icon { width: 64px; height: 64px; flex: none; }

  .web-band {
    position: absolute; left: 290px; right: 0; bottom: 0; height: 76px;
    background: var(--red);
    display: flex; align-items: center; justify-content: center;
    font-family: "Montserrat", sans-serif; font-weight: 600; font-size: 42px;
    color: var(--white);
    z-index: 1;
  }
</style>
</head>
<body>
  <section class="billboard">
    <div class="house-photo" role="img" aria-label="Soft greyscale photo of a two-storey house with trees"></div>

    <div class="brand">
      <span class="brand-name">VELMARK</span>
      <span class="brand-sub">PROPERTY GROUP</span>
    </div>

    <div class="ceo-photo" role="img" aria-label="Photo of the company CEO in a light blue shirt pointing up toward the headline"></div>

    <h1 class="headline">
      <span class="headline-main">Selling Your Home?</span>
      <span class="headline-sub">Get a Cash Offer, <span class="accent">Same Day.</span></span>
    </h1>

    <div class="offer-box">GET YOUR <span class="accent">FREE</span> OFFER</div>

    <div class="phone">
      <svg class="phone-icon" viewBox="0 0 58 58" aria-hidden="true">
        <circle cx="29" cy="29" r="29" fill="#f1141b"/>
        <path d="M19 15c2-1 4 0 5 2l3 6c1 2 0 3-1 4l-2 2c2 4 5 7 9 9l2-2c1-1 2-2 4-1l6 3c2 1 3 3 2 5l-2 3c-2 2-5 2-8 1-9-4-16-11-20-20-1-3-1-6 1-8z" fill="#ffffff"/>
        <path d="M33 17a10 10 0 0 1 9 9M33 11a16 16 0 0 1 15 15" stroke="#ffffff" stroke-width="3" fill="none" stroke-linecap="round"/>
      </svg>
      <span>865-555-0142</span>
    </div>

    <div class="web-band">www.velmarkpropertygroup.com</div>
  </section>
</body>
</html>
```